Business Card Re-Design/Update

We'd like to update out business cards. I've included our current "Style guide" which has the colour scheme of the organisation in it. I've also included the branding files with logos etc in them.

I've also included a copy of one of our existing cards so that you can see how ugly/dated they look. I'd like a fresh modern corporate look.

Target Market(s)

These are for our clients, potential clients, industry contacts - like all business cards

Contact Information for Business Card

Name
Position
Company Address - Level 1, 47 Garnet Lane, Toowong Qld 4066
Direct Phone
mobile
Email
Website -www.korvalnet.com.au
Logo

Colors

Designer to choose colors to be used in the design.

Requirements
Must have
• Main Logo
• Cards will need to be editable to be able to personalize them for each new employee.
Nice to have
• The MapOUT, HandOVER, UpKEEP would be okay to have if they can be sensibly and professionally added to the look without detracting from the main imagery.
• Maybe they could go on the back of the card? will leave this to your creative discretion as to whether/where they fit.
Should not have
• Should not have decorative or script fonts

```html
<!DOCTYPE html>
<html lang="en">
<head>
<meta charset="utf-8">
<title>Korvalnet Business Cards</title>
<link rel="stylesheet" href="https://fonts.googleapis.com/css2?family=Arimo:wght@400;700&display=swap">
<style>
  :root {
    --page: #161616;
    --card: #1f1f21;
    --card-edge: #2a2a2c;
    --brand-grey: #4d4d50;
    --text-grey: #8a8a8d;
    --text-light: #c9c9cb;
    --accent: #e3202a;
    --rule: #3a3a3d;
  }
  * { box-sizing: border-box; margin: 0; padding: 0; }
  html, body { width: 1200px; height: 900px; overflow: hidden; }
  body {
    background: var(--page);
    font-family: "Arimo", Arial, sans-serif;
    position: relative;
  }
  .card {
    position: absolute;
    width: 560px;
    height: 320px;
    background: var(--card);
    border: 1px solid var(--card-edge);
    border-radius: 22px;
    box-shadow: 0 18px 40px rgba(0,0,0,.55);
  }
  .card--back { left: 120px; top: 110px; }
  .card--front { left: 520px; top: 470px; }

  .wordmark {
    font-weight: 400;
    color: var(--brand-grey);
    letter-spacing: -1px;
    line-height: 1;
  }
  .card--back .wordmark {
    position: absolute;
    left: 170px; top: 110px;
    font-size: 62px;
  }
  .card--back .website {
    position: absolute;
    right: 48px; bottom: 60px;
    color: var(--accent);
    font-size: 14px;
    letter-spacing: 1px;
  }

  .brand {
    position: absolute;
    left: 150px; top: 62px;
    display: flex; align-items: center; gap: 14px;
  }
  .brand__mark {
    width: 34px; height: 34px;
    background: var(--accent);
  }
  .card--front .wordmark { font-size: 44px; }

  .divider {
    position: absolute;
    left: 190px; right: 40px; top: 128px;
    height: 1px; background: var(--rule);
  }
  .contact {
    position: absolute;
    right: 34px; top: 146px;
    list-style: none;
    text-align: right;
    color: var(--text-light);
    font-size: 14px;
    line-height: 21px;
  }
  .contact li { display: flex; justify-content: flex-end; align-items: center; gap: 7px; }
  .contact svg { width: 11px; height: 11px; fill: var(--accent); }
  .contact .email { margin-top: 14px; }

  .person {
    position: absolute;
    left: 40px; top: 196px;
  }
  .person__name {
    color: var(--accent);
    font-weight: 700;
    font-size: 19px;
    letter-spacing: .3px;
  }
  .person__role {
    color: var(--text-grey);
    font-size: 15px;
    margin-top: 3px;
  }
  .name-rule {
    position: absolute;
    left: 206px; right: 200px; top: 207px;
    height: 1px; background: var(--rule);
  }
  .address {
    position: absolute;
    left: 40px; top: 262px;
    font-style: normal;
    color: var(--text-grey);
    font-size: 15px;
    line-height: 20px;
  }
</style>
</head>
<body>
  <section class="card card--back" aria-label="Card back">
    <div class="wordmark">korvalnet</div>
    <div class="website">www.korvalnet.com.au</div>
  </section>

  <section class="card card--front" aria-label="Card front">
    <div class="brand">
      <span class="brand__mark"></span>
      <span class="wordmark">korvalnet</span>
    </div>
    <div class="divider"></div>

    <ul class="contact">
      <li>+61 (0)412 555 018
        <svg viewBox="0 0 12 12"><path d="M1 4c0-2 2-3 5-3s5 1 5 3l-2 1-1-1H4L3 5zM3 6h6l1 5H2z"/></svg></li>
      <li>+61 (0)7 3000 4121
        <svg viewBox="0 0 12 12"><path d="M3 0h6v12H3zM4 1v8h4V1z"/></svg></li>
      <li>+61 (0)7 3000 4122
        <svg viewBox="0 0 12 12"><path d="M3 0h6v4H3zM1 4h10v6H1zM3 8h6v4H3z"/></svg></li>
      <li class="email">dwhitlow@korvalnet.com.au
        <svg viewBox="0 0 12 12"><path d="M0 2h12v8H0zM1 3l5 4 5-4z"/></svg></li>
    </ul>

    <div class="person">
      <div class="person__name">DANA WHITLOW</div>
      <div class="person__role">Business Development Manager</div>
    </div>
    <div class="name-rule"></div>

    <address class="address">
      Level 1, 47 Garnet Lane<br>
      Toowong Qld 4066
    </address>
  </section>
</body>
</html>
```